Investment Memorandum Document

IM for Harbourline Lending Fund - is the document that needs work

Make sure it is all done in MS WORD so that i or lawyers can edit some words if required

the IM is NOT final but its 95% of the way there. Maybe a few more pages and wording changes - but that is something i can do i guess or you can easier adjust

Just to typeset and pretty it all up - a few sample finished products have been uploaded for reference.

KPT IM is the one i like - but feel free to show off your skills

put 1.2 to 1.8 all in contrasting row tables

Target Market(s)

Individual and Institutional investors with money

Industry/Entity Type

Investment Banking

Colors

Designer to choose colors to be used in the design.

Requirements
Must have
• clear professional layout and easy on the eye
• https://www.filebarn-example.net/sh/84m7t55xqk2wbnr/QQzdLeMu8RplbqTYAXNW47Ko?dl=0
• use the link above for high res images
Nice to have
• pictures and graphics
Should not have
• cartoons

```html
<!DOCTYPE html>
<html lang="en">
<head>
<meta charset="utf-8">
<title>Information Memorandum – Notice</title>
<link href="https://fonts.googleapis.com/css2?family=Roboto:wght@300;400&display=swap" rel="stylesheet">
<style>
  :root {
    --backdrop: #808080;
    --paper: #fafafa;
    --ink: #565656;
    --gold: #c6a06a;
    --footer-band: #3b3f41;
    --footer-ink: #ffffff;
  }
  * { margin: 0; padding: 0; box-sizing: border-box; }
  html, body {
    width: 1096px; height: 1200px; overflow: hidden;
    background: var(--backdrop);
    font-family: "Roboto", Arial, sans-serif;
  }
  .page {
    position: absolute; left: 219px; top: 135px;
    width: 658px; height: 929px;
    background: var(--paper);
  }
  .page-title {
    position: absolute; left: 48px; top: 78px;
    font-size: 18px; font-weight: 400; color: var(--gold);
  }
  .column {
    position: absolute; top: 108px; width: 265px; height: 748px;
    overflow: hidden;
    font-size: 10.6px; font-weight: 300; line-height: 14.6px; color: var(--ink);
    text-align: justify;
  }
  .column-left { left: 48px; }
  .column-right { left: 345px; }
  .column p { text-indent: 8px; margin-bottom: 3px; }
  .section-heading {
    font-size: 10.6px; font-weight: 400; color: var(--gold);
    text-transform: uppercase; padding-left: 8px; margin-bottom: 2px;
    letter-spacing: 0.1px;
  }
  .section-heading.wide { letter-spacing: 1.6px; }
  .page-footer-title {
    position: absolute; left: 48px; top: 879px;
    font-size: 10.6px; font-weight: 300; color: var(--ink);
  }
  .page-number {
    position: absolute; left: 526px; top: 872px; width: 132px; height: 29px;
    background: var(--footer-band); color: var(--footer-ink);
    display: flex; align-items: center; gap: 12px; padding-left: 14px;
    font-size: 11px; font-weight: 400;
  }
  .page-number .mark { width: 10px; height: 10px; border-radius: 50%; border: 1.5px solid var(--footer-ink); }
</style>
</head>
<body>
<main class="page">
  <h1 class="page-title">Notice</h1>

  <section class="column column-left">
    <p>This Information memorandum is dated XXX and is issued by Northgate Capital and Lending Corporation Pty Ltd ACN 152 884 307, holder of AFS licence number 418275, (Trustee), which is the trustee of the Diversified Commercial Income Fund (Fund).</p>
    <p>The purpose of this IM is to provide information for prospective investors to decide whether they wish to invest in the Fund.</p>
    <p>The Trustee has appointed Harbourline Asset Management Pty Ltd (Investment Manager) as the investment manager of the Fund under the Investment Management Agreement. The Investment Manager is an authorised representative (number 1274519XXX) of Northgate Capital and Lending Corporation Pty Ltd ACN 152 884 307 AFS licence number 418275. The purpose of this IM is to provide information for prospective Investors to decide whether they wish to invest in the Fund. The Fund’s trust deed (Trust Deed) provides for different Classes of Units. Under the Trust Deed, the different Classes of Units may have different rights and obligations. The performance of different Classes of Units may also differ depending on the investments of that Class. Holders of different Classes of Units will be treated fairly.</p>
    <h2 class="section-heading">No disclosure required</h2>
    <p>This IM is intended to provide potential Investors with information only and does not constitute a product disclosure statement or other disclosure document required by the Corporations Act 2001 (Cth) (Act). This IM has not been lodged with the Australian Securities and Investments Commission (ASIC) or any other government body.</p>
    <p>The offer made under this IM is only available to persons who qualify as wholesale clients (as defined in section 761G (7) of the Corporations Act) or sophisticated investors (as defined in section 761GA of the Corporations Act). (collectively, Qualified Investors). The Trustee will not issue Units in the Fund to a person unless it is satisfied that the person is a Qualified Investor.</p>
    <h2 class="section-heading">Restrictions on distribution</h2>
    <p>This IM does not constitute, and may not be used for the purposes of, an offer of Units or an invitation to apply to participate in the Fund by any person in any jurisdiction in which such offer or invitation is not authorised or in which the person endeavouring to make such offer or invitation is not qualified to do so or to any person to whom it is unlawful to make such an offer or invitation.</p>
  </section>

  <section class="column column-right">
    <p>No action has been taken to register or qualify interests in the Fund, the invitation to participate in the Fund, or to otherwise permit any public offering of Fund interests in any jurisdiction other than Australia. It is the responsibility of prospective Investors to satisfy themselves as to full compliance with the relevant laws and regulations of any jurisdiction in connection with any application to participate in the Fund, including obtaining any requisite governmental or other consent and adhering to any other formality prescribed in such jurisdiction.</p>
    <p>By receiving and viewing this IM, the recipient is warranting that they are legally entitled to do so and the securities laws of their relevant jurisdiction do no prohibit them from acquiring interests in the Fund. Further, the persons receiving and viewing this IM warrant that they are Qualified Investors.</p>
    <p>In particular, this product has not been and will not be registered under the US Securities Act or the securities laws of any state of the United States and may not be offered, sold, delivered or transferred in the United States or to, or for the account of, any “US Person” (as defined in Regulation S under the US Securities Act). Neither this IM, Application Form or other material relating to this product may be distributed in the United States. With respect to Australian jurisdiction, this IM have been prepared on the basis that the prospective Investors are wholesale clients or sophisticated investors, not retail clients within the meaning of the Corporations Act. Accordingly, this IM is not a product disclosure statement and does not contain all of the information that would be included in a product disclosure statement issued under the Corporations Act.</p>
    <p>The Trustee may in the future take actions to offer interests in the Fund in other jurisdictions.</p>
    <h2 class="section-heading wide">No responsibility for contents of document</h2>
    <p>To the maximum extent permitted by law, none of the Trustee, the Investment Manager, or any of their associates, related parties, directors, officers, employees, advisors (including financial, accounting and legal advisors) or representatives make any recommendation in relation to the Fund, or make any representation or warranty, express or implied, as to the accuracy, reliability or completeness of the information contained in this IM.</p>
    <p>This IM does not purport to contain all the information that a prospective Investor may require in evaluating a possible investment in the Fund.</p>
    <p>This IM must be read in conjunction with the Fund’s</p>
  </section>

  <footer>
    <div class="page-footer-title">Harbourline AM Diversified Commercial Income Fund – Information Memorandum</div>
    <div class="page-number"><span class="mark"></span><span>Page 2</span></div>
  </footer>
</main>
</body>
</html>
```